Flyer for the Lumen 2025 Conference

I am looking to produce a flyer for our upcoming conference, Lumen 2025. This is an annual conference that we plan to publicize on social media. The ideal designer will create a flyer that is eye-catching and effectively communicates the key information. Please see attached our logo, speaker photo, and flyer content.

Target Market(s)

All demographics

Industry/Entity Type

Christian

Font styles to use
Sans Serif

Requirements
Should not have
• Cross, church

```html
<!DOCTYPE html>
<html lang="en">
<head>
<meta charset="utf-8">
<title>Lumen 2025 Conference Flyer</title>
<link rel="stylesheet" href="https://fonts.googleapis.com/css2?family=Montserrat:wght@400;800;900&family=Open+Sans:wght@400;600;700&family=Dancing+Script:wght@500&display=swap">
<style>
  :root {
    --night: #0d1720;
    --ember: #c98a22;
    --gold: #e2b45a;
    --orange: #f59a0c;
    --white: #ffffff;
    --silver-hi: #f4f4f4;
    --silver-lo: #9a9a9a;
    --suit: #1d4e93;
  }
  * { margin: 0; padding: 0; box-sizing: border-box; }
  html, body { width: 960px; height: 1200px; overflow: hidden; background: var(--night); }
  .flyer {
    position: relative; width: 960px; height: 1200px; overflow: hidden;
    font-family: "Open Sans", sans-serif; color: var(--white);
    background:
      radial-gradient(ellipse 520px 460px at 760px 560px, rgba(214,150,40,.95), rgba(150,95,25,.55) 45%, transparent 75%),
      radial-gradient(ellipse 700px 500px at 600px 350px, rgba(120,85,30,.6), transparent 70%),
      linear-gradient(180deg, #0b1620 0%, #14202a 45%, #1a1d1c 100%);
  }
  .speaker-photo {
    position: absolute; left: 338px; top: 338px; width: 622px; height: 862px;
    background: radial-gradient(ellipse 260px 330px at 340px 210px, rgba(60,40,30,.55), transparent 70%),
                linear-gradient(180deg, transparent 0%, transparent 38%, rgba(29,78,147,.85) 55%, var(--suit) 100%);
  }
  .brand {
    position: absolute; top: 42px; left: 0; width: 960px; text-align: center;
    font-family: "Open Sans", sans-serif; font-weight: 600; font-size: 52px; letter-spacing: 1px; color: var(--white);
  }
  .brand-dot {
    display: block; width: 22px; height: 22px; border-radius: 50%;
    background: var(--orange); margin: 0 auto 4px;
  }
  .title {
    position: absolute; top: 158px; left: 0; width: 960px; text-align: center;
    font-family: "Montserrat", sans-serif; font-weight: 900; font-size: 134px; line-height: 1; letter-spacing: 1px;
    background: linear-gradient(180deg, var(--silver-hi) 15%, var(--silver-lo) 85%);
    -webkit-background-clip: text; background-clip: text; color: transparent;
  }
  .subtitle {
    position: absolute; top: 276px; left: 0; width: 960px; text-align: center;
    font-family: "Montserrat", sans-serif; font-weight: 400; font-size: 53px; color: var(--gold); letter-spacing: 1px;
  }
  .theme {
    position: absolute; top: 355px; left: 78px;
    font-family: "Dancing Script", cursive; font-weight: 500; font-size: 100px; line-height: 108px; color: var(--gold);
  }
  .speaker { position: absolute; top: 592px; left: 76px; }
  .speaker-role { font-size: 36px; line-height: 1.1; }
  .speaker-name { font-weight: 700; font-size: 56px; line-height: 1.15; }
  .schedule { position: absolute; top: 724px; left: 76px; }
  .session { margin-bottom: 22px; line-height: 1.1; }
  .session-day { font-size: 23px; text-transform: uppercase; }
  .session-date { font-weight: 700; font-size: 31px; }
  .session-time { font-size: 19px; }
  .venue {
    position: absolute; top: 1026px; left: 0; width: 960px; text-align: center;
  }
  .venue-name { color: var(--orange); font-weight: 700; font-size: 38px; line-height: 1.2; }
  .venue-address { font-size: 25px; line-height: 1.3; }
  .venue-contact { font-size: 19px; line-height: 1.6; }
  .venue-contact .sep { color: var(--orange); margin: 0 14px; font-weight: 700; }
  .app-note { font-size: 25px; margin-top: 14px; }
  .app-note strong { color: var(--orange); font-weight: 700; }
</style>
</head>
<body>
<main class="flyer">
  <div class="speaker-photo" role="img" aria-label="Portrait of the speaker in a blue blazer and beige turtleneck"></div>

  <div class="brand"><span class="brand-dot"></span>KAVEL</div>
  <h1 class="title">LUMEN 2025</h1>
  <p class="subtitle">A PROPHETIC CONFERENCE</p>
  <p class="theme">The Voice<br>of the Lord</p>

  <div class="speaker">
    <p class="speaker-role">Prophet</p>
    <p class="speaker-name">Elias Moreau</p>
  </div>

  <div class="schedule">
    <div class="session">
      <p class="session-day">Friday</p>
      <p class="session-date">December 26th</p>
      <p class="session-time">6:30PM - 9:00PM</p>
    </div>
    <div class="session">
      <p class="session-day">Saturday</p>
      <p class="session-date">December 27th</p>
      <p class="session-time">5:30PM - 8:00PM</p>
    </div>
    <div class="session">
      <p class="session-day">Sunday</p>
      <p class="session-date">December 29th</p>
      <p class="session-time">4:30PM - 7:00PM</p>
    </div>
  </div>

  <div class="venue">
    <p class="venue-name">The Harborview Performing Arts Center</p>
    <p class="venue-address">128 Linden Ridge Road, Eastfield, Maine 04011</p>
    <p class="venue-contact">207.555.0142<span class="sep">|</span>contact@kavel.org<span class="sep">|</span>www.kavel.org</p>
    <p class="app-note">Download the <strong>KAVEL App</strong> to stay updated on the event</p>
  </div>
</main>
</body>
</html>
```